Furniture Removalist needs Pinloop design

I already have a Pinloop page for my business.

I would like the style to match my logo and business card..

Let me know what other information you will need, as I'm not sure?

Industry/Entity Type

Business

```html
<!DOCTYPE html>
<html lang="en">
<head>
<meta charset="utf-8">
<title>KMT Removals – Pinloop page design</title>
<link rel="stylesheet" href="https://fonts.googleapis.com/css2?family=Open+Sans:wght@400;600;700&family=Arimo:wght@400;700&display=swap">
<style>
:root{
  --orange:#f26a21;
  --grey:#6d6e70;
  --grey-dark:#58595b;
  --bg:#eeeeee;
  --page-bg:#e9ebee;
  --bar:#3b5998;
  --link:#3b5998;
  --line:#dddfe2;
  --text:#1d2129;
  --muted:#90949c;
  --green:#42b72a;
  --white:#ffffff;
}
*{box-sizing:border-box;margin:0;padding:0}
html,body{width:1029px;height:1200px;overflow:hidden}
body{background:var(--bg);position:relative;font-family:'Open Sans',sans-serif;color:var(--text)}
.abs{position:absolute}

/* Page preview */
.page{left:130px;top:93px;width:733px;height:547px;background:var(--page-bg);overflow:hidden;font-family:'Arimo',sans-serif}
.topbar{left:0;top:0;width:733px;height:29px;background:var(--bar)}
.topbar .brand{left:10px;top:7px;color:var(--white);font-size:11px;font-weight:700}
.topbar .search{left:59px;top:7px;width:416px;height:15px;background:var(--white);border-radius:2px;font-size:10px;padding:1px 5px;color:var(--text)}
.topbar .nav{left:630px;top:8px;color:#d8dfea;font-size:8.5px;font-weight:700;word-spacing:8px}

.cover-sm{left:25px;top:30px;width:617px;height:165px;background:var(--white)}
.photo{background:linear-gradient(120deg,#e9c79a 0%,#d9a56c 45%,#b98452 100%)}
.cover-sm .photo{left:0;top:0;width:371px;height:165px}
.cover-sm .panel{left:371px;top:50px;width:246px;height:115px;background:var(--orange)}
.cover-sm .logo{left:335px;top:4px;display:flex;align-items:center;gap:6px}
.cover-sm .logo .mark{width:30px;height:30px;background:var(--grey)}
.cover-sm .logo .name{font-size:20px;color:var(--orange);line-height:1}
.services{list-style:none;color:var(--white)}
.services li{display:flex;align-items:center;white-space:nowrap}
.services li::before{content:"";display:inline-block;background:var(--white);border-radius:50%}
.cover-sm .services{left:348px;top:61px;font-size:10.5px}
.cover-sm .services li{height:14.6px}
.cover-sm .services li::before{width:7px;height:7px;margin-right:9px}
.contact{color:var(--white);display:flex;align-items:center;white-space:nowrap}
.cover-sm .phone{left:432px;top:151px;font-size:10px}
.cover-sm .abn{left:532px;top:153px;font-size:8px;font-weight:700}
.phone svg{margin-right:4px}

.band{left:25px;top:195px;width:617px;height:61px;background:var(--grey)}
.page-name{left:166px;top:205px;color:var(--white);font-size:16px;font-weight:700;letter-spacing:.5px}
.page-cat{left:166px;top:227px;color:var(--white);font-size:12px}
.btn{height:19px;top:229px;background:#f6f7f9;border:1px solid #ced0d4;font-size:8.5px;font-weight:700;color:#4b4f56;display:flex;align-items:center;justify-content:center}
.btn.like{left:436px;width:44px}
.btn.follow{left:487px;width:53px;color:var(--muted);font-weight:400}
.btn.message{left:542px;width:62px}
.btn.more{left:606px;width:27px}

.tabs{left:25px;top:256px;width:617px;height:33px;background:var(--white);border:1px solid var(--line)}
.tab{top:10px;font-size:10px;color:#4b4f56}
.tab.active{font-weight:700;color:var(--text)}
.tab.active::after{content:"";position:absolute;left:-4px;right:-4px;top:18px;height:2px;background:var(--link)}

.avatar-sm{left:38px;top:160px;width:120px;height:119px;background:var(--white);border:1px solid var(--line);padding:5px}

.side{left:649px;top:30px;width:84px;height:517px}
.create{left:0;top:7px;width:64px;height:16px;background:var(--green);color:var(--white);font-size:8px;font-weight:700;display:flex;align-items:center;justify-content:center;border-radius:2px}
.years{left:6px;top:37px;border-left:3px solid #cdd1d9;padding-left:5px;font-size:8.5px;color:var(--muted);line-height:17px}
.opened{left:659px;top:420px;border-left:3px solid #cdd1d9;padding-left:5px;font-size:8px;color:var(--muted)}

.card{background:var(--white);border:1px solid var(--line)}
.card-head{font-size:8px;font-weight:700;color:#4b4f56;padding:7px 8px;border-bottom:1px solid var(--line);display:flex;justify-content:space-between}
.people{left:25px;top:298px;width:238px;height:87px}
.likes{text-align:center;font-size:11px;padding:9px 0;border-bottom:1px solid var(--line)}
.likes b{font-size:12px}
.likes span{color:var(--muted)}
.invite-link{font-size:8.5px;color:var(--link);padding:7px 8px}
.about{left:25px;top:393px;width:238px;height:27px}
.composer{left:272px;top:298px;width:370px;height:71px}
.composer .tabs-row{font-size:9px;font-weight:700;padding:6px 9px;border-bottom:1px solid var(--line);display:flex;gap:14px}
.composer .tabs-row i{display:inline-block;width:10px;height:10px;margin-right:4px;vertical-align:-1px;border:1px solid var(--orange);background:#fde3d2}
.composer .tabs-row i.blue{border-color:var(--link);background:var(--link)}
.composer .hint{font-size:10px;color:var(--muted);padding:10px 9px}
.post{left:272px;top:375px;width:370px;height:45px;border-bottom:none}
.post .thumb{left:9px;top:10px;width:28px;height:28px;background:var(--grey)}
.post .who{left:44px;top:12px;font-size:8.5px;font-weight:700;color:var(--link)}
.post .when{left:44px;top:25px;font-size:8px;color:var(--muted)}

.composer2{left:25px;top:437px;width:298px;height:54px}
.composer2 .row{font-size:8.5px;font-weight:700;padding:8px 12px 4px;display:flex;gap:14px}
.composer2 .row i{display:inline-block;width:9px;height:9px;margin-right:3px;vertical-align:-1px;background:#8bc34a}
.composer2 .row i.o{background:#f0b35a}
.composer2 .field{margin:0 4px;border:1px solid #bdc7d8;height:19px;font-size:9.5px;color:var(--muted);padding:3px 4px}
.spine{left:333px;top:420px;width:2px;height:127px;background:#c4cde0}
.friends{left:345px;top:437px;width:297px;height:110px}
.friends .count{left:11px;top:9px;font-size:20px;font-weight:700;color:var(--link)}
.friends .label{left:42px;top:12px;font-size:8px;font-weight:700;color:var(--link);line-height:10px}
.friends .label span{display:block;font-weight:400;color:var(--muted)}
.friends .grid{left:11px;top:41px;width:273px;height:27px;display:flex;gap:2px}
.friends .grid i{flex:1;background:#b6c2dc}
.friends .grid b{width:27px;background:#b6c2dc;color:var(--link);font-size:11px;display:flex;align-items:center;justify-content:center}
.friends .inv{left:11px;top:80px;font-size:8px;font-weight:700;color:#4b4f56}
.friends .all{left:258px;top:80px;font-size:8px;color:var(--link)}
.friends .field{left:11px;top:93px;width:240px;height:14px;border:1px solid #bdc7d8;font-size:7.5px;color:var(--muted);padding:1px 3px}
.friends .go{left:253px;top:93px;width:31px;height:15px;background:#5b74a8;color:var(--white);font-size:8px;font-weight:700;display:flex;align-items:center;justify-content:center}

/* Profile image */
.avatar{left:40px;top:880px;width:148px;height:147px;background:var(--white);box-shadow:0 1px 3px rgba(0,0,0,.25);padding:7px}
.avatar-inner{width:100%;height:100%;border:2px solid var(--grey-dark);display:flex;flex-direction:column;align-items:center;justify-content:center;gap:8px}
.avatar-inner .mark{width:40px;height:40px;background:var(--orange)}
.avatar-inner .name{font-size:17px;font-weight:600;color:var(--grey-dark);text-align:center;line-height:1.15}
.avatar-sm .avatar-inner .mark{width:32px;height:32px}
.avatar-sm .avatar-inner .name{font-size:14px}
.caption{font-size:19px;color:#222}
.caption.profile{left:55px;top:1049px}

/* Cover */
.cover{left:237px;top:816px;width:729px;height:269px;background:var(--grey);box-shadow:0 2px 4px rgba(0,0,0,.3)}
.cover .photo{left:0;top:0;width:376px;height:196px}
.cover .top{left:376px;top:0;width:353px;height:59px;background:var(--white)}
.cover .panel{left:376px;top:59px;width:353px;height:137px;background:var(--orange)}
.cover .logo{left:420px;top:8px;display:flex;align-items:center;gap:7px}
.cover .logo .mark{width:38px;height:38px;background:var(--grey)}
.cover .logo .name{font-size:27px;color:var(--orange);line-height:1}
.cover .services{left:420px;top:64px;font-size:12.5px}
.cover .services li{height:17px}
.cover .services li::before{width:9px;height:9px;margin-right:13px}
.cover .phone{left:520px;top:178px;font-size:12px}
.cover .abn{left:629px;top:180px;font-size:10px;font-weight:700}
.caption.cover-cap{left:550px;top:1100px}
</style>
</head>
<body>

<section class="abs page" aria-label="Pinloop business page preview">
  <header class="abs topbar">
    <span class="abs brand">Pinloop</span>
    <div class="abs search">Your Brand</div>
    <span class="abs nav">Home Sam</span>
  </header>

  <div class="abs cover-sm">
    <div class="abs photo" role="img" aria-label="Photo of a couple unpacking cardboard moving boxes"></div>
    <div class="abs panel"></div>
    <div class="abs logo"><span class="mark"></span><span class="name">KMT Removals</span></div>
    <ul class="abs services">
      <li>Local, Country &amp; Interstate Removals</li>
      <li>Home &amp; Hi Rise Removals</li>
      <li>Office &amp; Factory Relocation's</li>
      <li>Pre - Packing &amp; Unpacking Service's</li>
      <li>Storage Solution</li>
    </ul>
    <div class="abs contact phone"><svg width="11" height="9" viewBox="0 0 12 10"><path d="M1 3 Q6 -1 11 3 L10 5 L8 4 L8 3 Q6 2 4 3 L4 4 L2 5 Z M3 5 H9 L10 9 H2 Z" fill="#fff"/></svg>0412555019</div>
    <div class="abs contact abn">ABN: 12345678901</div>
  </div>

  <div class="abs band"></div>
  <div class="abs page-name">KMT REMOVALS</div>
  <div class="abs page-cat">Transport/Freight</div>
  <div class="abs btn like">Like</div>
  <div class="abs btn follow">+ Follow</div>
  <div class="abs btn message">Message</div>
  <div class="abs btn more">•••</div>

  <nav class="abs tabs">
    <span class="abs tab active" style="left:145px">Timeline</span>
    <span class="abs tab" style="left:211px">About</span>
    <span class="abs tab" style="left:261px">Photos</span>
    <span class="abs tab" style="left:317px">Likes</span>
  </nav>

  <div class="abs avatar-sm"><div class="avatar-inner"><span class="mark"></span><span class="name">KMT<br>Removals</span></div></div>

  <aside class="abs side">
    <div class="abs create">Create Page</div>
    <div class="abs years">Recent<br>2014<br>Launched</div>
  </aside>
  <div class="abs opened">Opened</div>

  <div class="abs card people">
    <div class="card-head"><span>PEOPLE</span><span>›</span></div>
    <div class="likes"><b>48</b> <span>likes</span></div>
    <div class="invite-link">Invite your friends to like this Page</div>
  </div>
  <div class="abs card about"><div class="card-head" style="border:none"><span>ABOUT</span><span>›</span></div></div>

  <div class="abs card composer">
    <div class="tabs-row"><span><i class="blue"></i>Post</span><span><i></i>Photo / Video</span></div>
    <div class="hint">Write something on this Page...</div>
  </div>
  <div class="abs card post">
    <div class="abs thumb"></div>
    <div class="abs who">KMT REMOVALS</div>
    <div class="abs when">June 19</div>
  </div>

  <div class="abs card composer2">
    <div class="row"><span><i></i>Post</span><span><i class="o"></i>Photo</span></div>
    <div class="field">Write something...</div>
  </div>
  <div class="abs spine"></div>
  <div class="abs card friends">
    <div class="abs count">39</div>
    <div class="abs label">Friends<span>Like Your Brand</span></div>
    <div class="abs grid"><i></i><i></i><i></i><i></i><i></i><i></i><i></i><i></i><i></i><b>+30</b></div>
    <div class="abs inv">Invite Your Friends to Like this Page</div>
    <div class="abs all">See All</div>
    <div class="abs field">Type a friend's name...</div>
    <div class="abs go">Invite</div>
  </div>
</section>

<div class="abs avatar"><div class="avatar-inner"><span class="mark"></span><span class="name">KMT<br>Removals</span></div></div>
<div class="abs caption profile">Profile Image</div>

<section class="abs cover" aria-label="Cover">
  <div class="abs photo" role="img" aria-label="Photo of a couple unpacking cardboard moving boxes"></div>
  <div class="abs top"></div>
  <div class="abs panel"></div>
  <div class="abs logo"><span class="mark"></span><span class="name">KMT Removals</span></div>
  <ul class="abs services">
    <li>Local, Country &amp; Interstate Removals</li>
    <li>Home &amp; Hi Rise Removals</li>
    <li>Office &amp; Factory Relocation's</li>
    <li>Pre - Packing &amp; Unpacking Service's</li>
    <li>Storage Solution</li>
  </ul>
  <div class="abs contact phone"><svg width="14" height="11" viewBox="0 0 12 10"><path d="M1 3 Q6 -1 11 3 L10 5 L8 4 L8 3 Q6 2 4 3 L4 4 L2 5 Z M3 5 H9 L10 9 H2 Z" fill="#fff"/></svg>0412555019</div>
  <div class="abs contact abn">ABN: 12345678901</div>
</section>
<div class="abs caption cover-cap">Pinloop Cover</div>

</body>
</html>
```